Business Card Re-Design

Consulting Company: To build a high performance organization, you need great leaders at all levels throughout your organization. The Northvale Talent Growth Studio engages, inspires, and educates current and future leaders to step beyond the ordinary and deliver exceptional results. This new breed of leaders will motivate your staff to leave the safety of complacency behind and come together to build an extraordinary organization. The current trend has been to ask our people to do more with fewer resources. People have been stepping up to the challenge, but more is required to ensure success with a new work paradigm. We work with your management team to build a successful strategy that will make your organization more effective. NTGS then supports your management team by providing a comprehensive set of proven services to empower your entire organization to successfully execute new strategies.Let NTGS help you optimize your organization’s individual and team performance today!

Target Market(s)

Federal, State and Local Government / Non profit

Industry/Entity Type

Management Consulting

Contact Information for Business Card

NTGS, inc (Northvale Talent Growth Studio) Optimizing Individual and Organizational Performance

Colors
fee18a
ec1f27
474747
fbf289

Requirements
Must have
• Professional and high quality feel

```html
<!DOCTYPE html>
<html lang="en">
<head>
<meta charset="utf-8">
<title>Northvale Talent Growth Studio – Business Card</title>
<link href="https://fonts.googleapis.com/css2?family=Tinos:wght@400;700&family=Arimo:wght@400&display=swap" rel="stylesheet">
<style>
  :root {
    --backdrop: #2e2825;
    --card: #141414;
    --gold: #c9a45a;
    --gold-soft: #b8954d;
    --silver: #a9a9a6;
    --rule: #5a5a58;
    --ink: #f2f2f2;
    --icon-glyph: #141414;
  }
  * { margin: 0; padding: 0; box-sizing: border-box; }
  html, body { width: 1200px; height: 780px; overflow: hidden; }
  body { background: var(--backdrop); position: relative; }

  .card {
    position: absolute;
    left: 75px; top: 90px;
    width: 1050px; height: 600px;
    background: radial-gradient(ellipse at 35% 40%, #1d1d1d 0%, var(--card) 70%);
    box-shadow: 0 18px 40px rgba(0,0,0,.45);
  }

  .brand {
    position: absolute;
    left: 40px; top: 110px;
    width: 430px;
    text-align: center;
  }
  .brand-mark {
    display: block;
    margin: 0 auto 34px;
    width: 96px; height: 96px;
    border-radius: 50%;
    border: 5px solid var(--silver);
  }
  .brand-name {
    font-family: "Tinos", serif;
    font-weight: 400;
    color: var(--gold);
    font-size: 34px;
    line-height: 1.25;
    letter-spacing: 1px;
    font-variant: small-caps;
  }
  .brand-rule {
    display: flex; align-items: center; gap: 18px;
    margin-top: 8px;
  }
  .brand-rule::before, .brand-rule::after {
    content: ""; flex: 1; height: 2px; background: var(--rule);
  }
  .brand-rule span { display: block; }

  .divider {
    position: absolute;
    left: 505px; top: 60px;
    width: 3px; height: 480px;
    background: var(--gold);
  }

  .person {
    position: absolute;
    left: 545px; top: 72px;
    font-family: "Tinos", serif;
    color: var(--gold);
  }
  .person-name { font-size: 36px; font-weight: 700; letter-spacing: .5px; }
  .person-title { font-size: 19px; font-weight: 700; color: var(--gold-soft); margin-top: 0; }

  .contacts {
    position: absolute;
    left: 548px; top: 285px;
    list-style: none;
    font-family: "Arimo", sans-serif;
    font-size: 22px;
    color: var(--ink);
  }
  .contacts li { display: flex; align-items: center; gap: 14px; height: 36px; }
  .contacts svg { width: 18px; height: 18px; flex: none; }
</style>
</head>
<body>
  <section class="card">
    <div class="brand">
      <span class="brand-mark"></span>
      <div class="brand-name">Northvale Talent</div>
      <div class="brand-rule"><span class="brand-name">Growth Studio</span></div>
    </div>

    <div class="divider"></div>

    <div class="person">
      <div class="person-name">Marcus L. Whitfield</div>
      <div class="person-title">President &amp; CEO</div>
    </div>

    <ul class="contacts">
      <li>
        <svg viewBox="0 0 18 18"><rect width="18" height="18" rx="2" fill="#c9a45a"/><path d="M5 4c1 0 2 2 2 3s-1 1-1 2 2 3 3 3 1-1 2-1 3 1 3 2-1 2-2 2C8 15 3 10 3 6c0-1 1-2 2-2z" fill="#141414"/></svg>
        555-014-2281
      </li>
      <li>
        <svg viewBox="0 0 18 18"><rect width="18" height="18" rx="2" fill="#c9a45a"/><rect x="6" y="3" width="6" height="12" rx="1" fill="#141414"/></svg>
        555-014-7730
      </li>
      <li>
        <svg viewBox="0 0 18 18"><rect width="18" height="18" rx="2" fill="#c9a45a"/><rect x="3.5" y="5" width="11" height="8" fill="#141414"/><path d="M3.5 5l5.5 4.5L14.5 5" stroke="#c9a45a" stroke-width="1.2" fill="none"/></svg>
        mwhitfield@ntgsinc.com
      </li>
      <li>
        <svg viewBox="0 0 18 18"><rect width="18" height="18" rx="2" fill="#c9a45a"/><circle cx="9" cy="9" r="5.5" fill="none" stroke="#141414" stroke-width="1.5"/><path d="M3.5 9h11M9 3.5c-3 3-3 8 0 11M9 3.5c3 3 3 8 0 11" stroke="#141414" stroke-width="1.2" fill="none"/></svg>
        www.ntgsinc.com
      </li>
      <li>
        <svg viewBox="0 0 18 18"><rect width="18" height="18" rx="2" fill="#c9a45a"/><path d="M9 15s-4-4.5-4-7.5a4 4 0 0 1 8 0C13 10.5 9 15 9 15z" fill="#141414"/><circle cx="9" cy="7.5" r="1.5" fill="#c9a45a"/></svg>
        PO Box 4180 Fairhaven, MD 20899
      </li>
    </ul>
  </section>
</body>
</html>
```